Web Design Project

We need a web design for a new company. We have a logo, and we've identified the style of a website that we'd like to adapt (www.tovendrafield.example). We do not sell to the public. The purpose of the site is (1) to allow our appointed sales partners to log in to our proprietary database system and (2) to provide a basic web presence and some basic information about our company.

We sell business insurance through independent agents - our sales partners.

Please do not use a photo of a person/s as a central design element, or at all.

Target Market(s)

The purpose of the site is not to sell, but to provide a professional landing page for a log in and some basic company information.

Industry/Entity Type

Business

Requirements
Must have
• A professional look. Agent log in must be central, clear and easy. Use of our logo and our colors.
Should not have
• Photos of people

```html
<!DOCTYPE html>
<html lang="en">
<head>
<meta charset="utf-8">
<title>Alder Creek Insurance</title>
<link rel="stylesheet" href="https://fonts.googleapis.com/css2?family=PT+Sans:wght@400;700&family=PT+Sans+Narrow:wght@400;700&family=Arimo:ital@1&display=swap">
<style>
  :root {
    --hero-deep: #0f3c58;
    --hero-mid: #1d5f84;
    --hero-glow: #3f93bd;
    --nav-band: #0c2233;
    --accent: #3fbde6;
    --accent-soft: #55c6ec;
    --white: #ffffff;
    --login-bg: #ececec;
    --login-label: #3a6d8f;
    --field-border: #c9c9c9;
    --arrow-btn: #6aa9d6;
    --card-head: #0b1a24;
    --rule: #d6d6d6;
    --title: #333333;
    --body: #6a6a6a;
    --footer: #4a4a4a;
    --footer-top: #333333;
  }
  * { margin: 0; padding: 0; box-sizing: border-box; }
  html, body { width: 1200px; height: 1029px; overflow: hidden; background: var(--white); }
  .page { position: relative; width: 1200px; height: 1029px; font-family: "PT Sans", sans-serif; }
  .abs { position: absolute; }

  .hero {
    left: 0; top: 0; width: 1200px; height: 463px;
    background: radial-gradient(ellipse 520px 380px at 400px 260px, var(--hero-glow), var(--hero-mid) 55%, var(--hero-deep));
  }
  .nav-band { left: 0; top: 24px; width: 1200px; height: 61px; background: var(--nav-band); opacity: .92; }
  .brand { left: 197px; top: 41px; display: flex; align-items: center; gap: 8px;
    font-family: "PT Sans Narrow", sans-serif; font-weight: 700; font-size: 17px; color: var(--white); }
  .brand-mark { width: 16px; height: 16px; background: var(--accent); }
  .nav a { position: absolute; top: 47px; font-family: "PT Sans Narrow", sans-serif; font-weight: 700;
    font-size: 13px; letter-spacing: .5px; color: var(--accent); text-decoration: none; text-transform: uppercase; }
  .nav a.current { color: var(--white); }

  .hero-visual { left: 218px; top: 94px; width: 339px; height: 369px;
    background: radial-gradient(ellipse at 50% 45%, #8fc6de, #3d87b0 60%, rgba(29,95,132,0) 100%); }

  .headline { left: 650px; top: 158px; font-size: 31px; line-height: 36px; color: var(--accent); font-weight: 400; }
  .headline span { display: block; color: var(--white); }
  .subhead { left: 650px; top: 238px; font-size: 18px; color: var(--accent-soft); }
  .dots { left: 650px; top: 270px; width: 353px; border-top: 1px dotted #4f8fb2; }
  .intro { left: 650px; top: 280px; width: 360px; font-family: "PT Sans Narrow", sans-serif;
    font-size: 14px; line-height: 19px; color: var(--white); }
  .btn-primary { left: 650px; top: 354px; width: 84px; height: 33px; background: var(--accent);
    color: var(--white); font-family: "PT Sans Narrow", sans-serif; font-size: 14px; line-height: 33px; text-align: center; }

  .login { left: 0; top: 463px; width: 1200px; height: 64px; background: var(--login-bg); border-bottom: 1px solid #d9d9d9; }
  .login-label { top: 488px; font-family: "Arimo", sans-serif; font-style: italic; font-size: 12px; letter-spacing: .5px; color: var(--login-label); }
  .field { top: 481px; height: 28px; background: var(--white); border: 1px solid var(--field-border); }
  .field-go { left: 791px; top: 481px; width: 29px; height: 28px; background: var(--arrow-btn); }
  .divider-v { left: 847px; top: 481px; height: 30px; border-left: 2px dotted #b8b8b8; }
  .btn-register { left: 875px; top: 480px; width: 103px; height: 30px; background: linear-gradient(#fdfdfd, #e9e9e9);
    border: 1px solid #d0d0d0; font-family: "Arimo", sans-serif; font-size: 12px; letter-spacing: .5px;
    color: var(--login-label); text-align: center; line-height: 28px; }

  .card { top: 570px; width: 238px; }
  .card-head { height: 32px; background: var(--card-head); color: var(--white); font-weight: 700; font-size: 15px; line-height: 32px; text-align: center; }
  .card-visual { margin-top: 5px; height: 122px; background: linear-gradient(#4f5a63, #8a8678 55%, #7a6f45); }
  .card-title { margin-top: 13px; border-top: 1px solid var(--rule); border-bottom: 1px solid var(--rule);
    height: 32px; line-height: 31px; font-size: 18px; color: var(--title); letter-spacing: .3px; }
  .card-text { margin-top: 10px; font-family: "PT Sans Narrow", sans-serif; font-size: 14px; line-height: 20.5px; color: var(--body); }
  .card-more { margin-top: 16px; display: flex; align-items: center; gap: 6px; font-family: "PT Sans Narrow", sans-serif; font-size: 13px; color: var(--accent); }

  .footer { left: 0; top: 956px; width: 1200px; height: 73px; background: var(--footer); border-top: 6px solid var(--footer-top); }
  .copyright { left: 171px; top: 984px; font-family: "PT Sans Narrow", sans-serif; font-size: 12.5px; color: var(--white); }
  .copyright em { font-style: normal; color: var(--accent); }
  .footer-nav a { position: absolute; top: 984px; font-family: "PT Sans Narrow", sans-serif; font-size: 12.5px; color: var(--white); text-decoration: none; }
  .footer-nav a.highlight { color: var(--accent); }
</style>
</head>
<body>
<div class="page">
  <div class="abs hero"></div>
  <div class="abs nav-band"></div>
  <div class="abs brand"><span class="brand-mark"></span>Alder Creek Insurance</div>
  <nav class="nav">
    <a class="current" style="left:583px">Home</a>
    <a style="left:652px">About</a>
    <a style="left:722px">Services</a>
    <a style="left:806px">Our Work</a>
    <a style="left:898px">Blog</a>
    <a style="left:959px">Contact</a>
  </nav>

  <div class="abs hero-visual" role="img" aria-label="Portrait photo of a business adviser in a suit"></div>

  <h1 class="abs headline">Sungelle Molestielle<span>Fore Refed Berreferid</span></h1>
  <p class="abs subhead">Proin vehicula pulvinar nisi ac semper</p>
  <div class="abs dots"></div>
  <p class="abs intro">Lorem ipsum dolor sit amet, consectetur adipiscing elit. Praesent dolor nunc, rhoncus porttitor bibendum in, placerat sed dui rae-sent suscipit consequat nunc, et accumsan arcu.</p>
  <div class="abs btn-primary">read more</div>

  <div class="abs login"></div>
  <span class="abs login-label" style="left:209px">Login User</span>
  <div class="abs field" style="left:288px;width:211px"></div>
  <span class="abs login-label" style="left:539px">Password</span>
  <div class="abs field" style="left:609px;width:182px"></div>
  <div class="abs field-go">
    <svg width="29" height="28" viewBox="0 0 29 28"><path d="M13 10 L17 14 L13 18 Z" fill="#fff"/></svg>
  </div>
  <div class="abs divider-v"></div>
  <div class="abs btn-register">Register</div>

  <article class="abs card" style="left:197px">
    <div class="card-head">Lorem Ipsum</div>
    <div class="card-visual" role="img" aria-label="Photo of a person with an umbrella in a field under stormy sky"></div>
    <h2 class="card-title">Lorem Ipsum Dolor</h2>
    <p class="card-text">Lorem ipsum dolor sit amet, consectetur adipis ing elit. Praesent dolor nunc, rhoncus portti-torol bibendum in, placerat sed dui raesent suscipiten consequat nunc.</p>
    <div class="card-more">read more <svg width="12" height="8" viewBox="0 0 12 8"><path d="M0 4H10M7 1L10 4L7 7" stroke="#3fbde6" stroke-width="1.3" fill="none"/></svg></div>
  </article>
  <article class="abs card" style="left:483px">
    <div class="card-head">Lorem Ipsum</div>
    <div class="card-visual" role="img" aria-label="Photo of a person with an umbrella in a field under stormy sky"></div>
    <h2 class="card-title">Lorem Ipsum Dolor</h2>
    <p class="card-text">Lorem ipsum dolor sit amet, consectetur adipis ing elit. Praesent dolor nunc, rhoncus portti-torol bibendum in, placerat sed dui raesent suscipiten consequat nunc.</p>
    <div class="card-more">read more <svg width="12" height="8" viewBox="0 0 12 8"><path d="M0 4H10M7 1L10 4L7 7" stroke="#3fbde6" stroke-width="1.3" fill="none"/></svg></div>
  </article>
  <article class="abs card" style="left:766px">
    <div class="card-head">Lorem Ipsum</div>
    <div class="card-visual" role="img" aria-label="Photo of a person with an umbrella in a field under stormy sky"></div>
    <h2 class="card-title">Lorem Ipsum Dolor</h2>
    <p class="card-text">Lorem ipsum dolor sit amet, consectetur adipis ing elit. Praesent dolor nunc, rhoncus portti-torol bibendum in, placerat sed dui raesent suscipiten consequat nunc.</p>
    <div class="card-more">read more <svg width="12" height="8" viewBox="0 0 12 8"><path d="M0 4H10M7 1L10 4L7 7" stroke="#3fbde6" stroke-width="1.3" fill="none"/></svg></div>
  </article>

  <footer class="abs footer"></footer>
  <p class="abs copyright">Copyright © 2012 <em>fernlight</em> design &nbsp;|&nbsp; All rights reserved</p>
  <nav class="footer-nav">
    <a style="left:824px">Home</a>
    <a style="left:883px">About</a>
    <a style="left:940px">Contact</a>
    <a class="highlight" style="left:1004px">Login</a>
  </nav>
</div>
</body>
</html>
```